AI Layout work for Business Cards, Letterhead and Compliment Slip for Award-winning UK Property Deve

No actual logo or corporate identity design work needed here but some skill required to create layouts for business card, letterhead and compliment slip for this award-winning company.
I can provide AI files featuring the company logo and an initial layout of the business card, (6 versions featuring the same design but for different personnel), along with some initial instructions (with possibly more to follow from the client). The finished layouts for each item need to be print-ready in AI format - 8 in all (6 for each business card plus 1 for letterhead and 1 for compliment slip).
I've given this project a 5-day duration but there may be some flexibility built into that depending on client feedback. Hopefully that won't be a problem.
UPDATE:
The client has been very prescriptive about the layout and design of these. To that end, please find 3 additional pdfs that explain what's required.
1.
All BUSINESS CARDS need to be laid out as per the attached AI file (but see latest pdf to check which layout - there are 2 in the original AI file). Use the details in the RUNE-contact-details.pdf to create 6 individual AI files, one for each card.
2.
Create 2 additional AI files, one each for the LETTERHEAD and the COMPLIMENT SLIP based on the latest mock-up that I've provided (letterhead-layout-final.pdf)
In all, I need EIGHT individual AI files, 6 for each business card, 1 for the letterhead and 1 for the compliment slip. I'd like to get this done as soon as possible now please.
Target Market(s)
Purchasers of upmarket luxury properties - see here: http://www.runeestates.co.uk
Industry/Entity Type
Business
Requirements
Must have
- Layouts need to be cool, understated and uncluttered.
Nice to have
- Please keep it simple! The actual logo background colour is likely to change (awaiting confirmation from client) but accompanying text detail and font (Deja Vu Sans Condensed) can remain as seen in the files below - for the time being at least! That having been said, I'm open to suggestions.
Should not have
- Nothing extreme or ostentatious please.

```html
<!DOCTYPE html>
<html lang="en">
<head>
<meta charset="utf-8">
<title>RUNE Urban Estates – Stationery</title>
<link href="https://fonts.googleapis.com/css2?family=Encode+Sans+Condensed:wght@400;600&display=swap" rel="stylesheet">
<style>
  :root {
    --navy: #1b1e4b;
    --slate: #4a4a4d;
    --paper: #ffffff;
    --backdrop: #e4e5e7;
    --ink: #1b1e4b;
    --rule: #8e90a8;
    --light-text: #e9eaf2;
  }
  * { margin: 0; padding: 0; box-sizing: border-box; }
  html, body { width: 1200px; height: 1000px; overflow: hidden; }
  body {
    background: var(--backdrop);
    font-family: "Encode Sans Condensed", "Arial Narrow", sans-serif;
    position: relative;
  }
  .sheet { position: absolute; box-shadow: 0 2px 8px rgba(0,0,0,0.12); }

  /* Letterhead */
  .letterhead {
    left: 50px; top: 160px; width: 480px; height: 679px;
    background: var(--paper);
  }
  .wordmark { text-align: center; color: var(--ink); }
  .wordmark__name { font-weight: 600; letter-spacing: 1px; line-height: 1; }
  .wordmark__sub {
    text-transform: uppercase; letter-spacing: 1.5px;
    border-top: 1px solid currentColor; display: inline-block; padding-top: 2px;
  }
  .letterhead .wordmark { position: absolute; top: 40px; left: 0; right: 0; }
  .letterhead .wordmark__name { font-size: 34px; }
  .letterhead .wordmark__sub { font-size: 8px; }
  .letterhead__footer {
    position: absolute; left: 40px; right: 40px; bottom: 40px;
    border-top: 1px solid var(--ink); border-bottom: 1px solid var(--ink);
    padding: 12px 0; text-align: center; color: var(--ink);
    font-size: 8.5px; line-height: 1.8; letter-spacing: 0.3px;
  }

  /* Business cards */
  .card { width: 280px; height: 182px; background: var(--navy); color: var(--light-text); overflow: hidden; }
  .card--front { left: 590px; top: 70px; }
  .card--back { left: 890px; top: 70px; }
  .card__diagonal {
    position: absolute; inset: 0; background: var(--slate);
    clip-path: polygon(0 0, 42% 0, 20% 100%, 0 100%);
  }
  .card--back .wordmark { position: absolute; left: 120px; top: 62px; color: var(--light-text); }
  .card--back .wordmark__name { font-size: 30px; }
  .card--back .wordmark__sub { font-size: 7px; }
  .card__person { position: absolute; left: 22px; top: 26px; }
  .card__name { font-size: 10px; letter-spacing: 1.5px; text-transform: uppercase; }
  .card__role { font-size: 10px; margin-top: 2px; }
  .card--front .wordmark { position: absolute; right: 22px; top: 64px; color: var(--light-text); }
  .card--front .wordmark__name { font-size: 16px; }
  .card--front .wordmark__sub { font-size: 4.5px; letter-spacing: 0.8px; }
  .card__contact { position: absolute; left: 22px; top: 72px; font-size: 7px; line-height: 1.55; }
  .card__rule { position: absolute; left: 22px; right: 22px; top: 118px; border-top: 1px solid var(--rule); }
  .card__address { position: absolute; left: 22px; top: 126px; font-size: 7px; line-height: 1.55; }

  /* Compliment slip */
  .slip { left: 590px; top: 300px; width: 280px; height: 400px; background: var(--navy); color: var(--light-text); overflow: hidden; }
  .slip .card__diagonal { clip-path: polygon(0 0, 78% 0, 10% 100%, 0 100%); }
  .slip .wordmark { position: absolute; left: 40px; top: 50px; color: var(--light-text); }
  .slip .wordmark__name { font-size: 46px; }
  .slip .wordmark__sub { font-size: 10px; }
  .slip__greeting { position: absolute; left: 40px; top: 138px; font-size: 17px; }
  .slip__contact { position: absolute; left: 40px; top: 184px; font-size: 9px; line-height: 1.6; }
  .slip__rule { position: absolute; left: 40px; right: 40px; top: 240px; border-top: 1px solid var(--rule); }
  .slip__address { position: absolute; left: 40px; top: 250px; font-size: 9px; line-height: 1.6; }

  /* Envelope */
  .envelope { left: 890px; top: 300px; width: 280px; height: 140px; background: var(--paper); }
</style>
</head>
<body>

  <section class="sheet letterhead" aria-label="Letterhead">
    <div class="wordmark">
      <div class="wordmark__name">RUNE</div>
      <div class="wordmark__sub">Urban Estates</div>
    </div>
    <footer class="letterhead__footer">
      <div>T: +44 (0)1632 960418 &nbsp;E: enquiries@runeestates.co.uk &nbsp;W: runeestates.co.uk</div>
      <div>• RUNE Exclusive Estates • Ashby Court House • Ashby Lane • Little Marden • HX9 2QT</div>
    </footer>
  </section>

  <section class="sheet card card--front" aria-label="Business card front">
    <div class="card__person">
      <div class="card__name">Martin Hale</div>
      <div class="card__role">Director</div>
    </div>
    <div class="wordmark">
      <div class="wordmark__name">RUNE</div>
      <div class="wordmark__sub">Urban Estates</div>
    </div>
    <div class="card__contact">
      T: +44 (0)1632 960418<br>
      E: enquiries@runeestates.co.uk<br>
      W: runeestates.co.uk
    </div>
    <div class="card__rule"></div>
    <div class="card__address">
      • RUNE Exclusive Estates<br>
      • Ashby Court House • Ashby Lane<br>
      • Little Marden • HX9 2QT
    </div>
  </section>

  <section class="sheet card card--back" aria-label="Business card back">
    <div class="card__diagonal"></div>
    <div class="wordmark">
      <div class="wordmark__name">RUNE</div>
      <div class="wordmark__sub">Urban Estates</div>
    </div>
  </section>

  <section class="sheet slip" aria-label="Compliment slip">
    <div class="card__diagonal"></div>
    <div class="wordmark">
      <div class="wordmark__name">RUNE</div>
      <div class="wordmark__sub">Urban Estates</div>
    </div>
    <p class="slip__greeting">With Compliments</p>
    <div class="slip__contact">
      T: +44 (0)1632 960418<br>
      E: enquiries@runeestates.co.uk<br>
      W: runeestates.co.uk
    </div>
    <div class="slip__rule"></div>
    <div class="slip__address">
      • RUNE Exclusive Estates<br>
      • Ashby Court House • Ashby Lane<br>
      • Little Marden • HX9 2QT
    </div>
  </section>

  <section class="sheet envelope" aria-label="Envelope"></section>

</body>
</html>
```